Mirabo & Orvan Automotive Repair Shop. Need a new website design.

We specialize in Mirabo & Orvan auto repair, but also work on other Asian import vehicles. We have been in business for 7 years and pride ourselves on high quality auto repair that is fixed right the first time. Would like the automotive repair website to incorporate the colors black, red and white if possible and have our logo and some Mirabo and Orvan vehicles included in the website.

Target Market(s)

Mirabo & Orvan vehicle owners

Industry/Entity Type

Automotive Repair

Coding

Coded - Design and coding required

Number of Pages Required

5+ page

Colors
EB3D1F
EC4F4E
F09395
F8D3D4
FCEDEE

Requirements
Must have
• Home, Services, Contact Us, Schedule appointment, and a gallery tab that I can add shop pictures to when completed.
Nice to have
• Would like to see example pictures of job next to each service listed.
Should not have
• Service not related to auto repair. Ex. auto detailing, towing, car wash

```html
<!DOCTYPE html>
<html lang="en">
<head>
<meta charset="utf-8">
<title>Calder Automotive – Contact</title>
<link rel="stylesheet" href="https://fonts.googleapis.com/css2?family=Fira+Sans+Extra+Condensed:ital,wght@0,400;0,500;0,600;1,400&family=Open+Sans:ital,wght@0,400;0,600;0,700;1,400&display=swap">
<style>
:root{
  --red:#e30613;
  --black:#000;
  --ink:#111;
  --muted:#444;
  --field:#f1f1f1;
  --white:#fff;
  --head:"Fira Sans Extra Condensed",sans-serif;
  --body:"Open Sans",sans-serif;
}
*{box-sizing:border-box;margin:0;padding:0}
html,body{width:790px;height:1200px;overflow:hidden;background:var(--white)}
body{position:relative;font-family:var(--body);color:var(--ink)}
.abs{position:absolute}
svg{display:block}

/* header */
.header{left:0;top:0;width:790px;height:80px;background:var(--black)}
.brand{left:84px;top:22px;display:flex;align-items:center;gap:5px;color:var(--white);font-family:var(--body);font-weight:700;font-size:11px;letter-spacing:.5px}
.brand .dot{width:14px;height:14px;border-radius:50%;background:var(--red)}
.badge-top{top:14px;display:flex;align-items:center;gap:6px}
.icon-ring{width:23px;height:23px;border-radius:50%;background:#ddd;border:2px solid #888;display:flex;align-items:center;justify-content:center}
.badge-top .txt{font-family:var(--head);font-style:italic;font-size:10px;line-height:11px;color:#eee}
.badge-top .txt b{color:var(--red);font-weight:600}
.stars{color:var(--red);font-size:11px;letter-spacing:0}
.nav{top:62px;left:383px;display:flex;gap:0;font-family:var(--body);font-weight:700;font-size:7.3px;color:var(--white)}
.nav span{margin-right:21px}
.nav .active{color:var(--red);margin-right:0}

/* hero */
.hero{left:0;top:80px;width:790px;height:208px;background:linear-gradient(180deg,#bfc1c3 0%,#8e8f92 45%,#6b6a6a 100%)}
.hero-text{left:73px;top:150px;color:var(--white)}
.hero-text .kicker{font-family:var(--head);font-size:7.5px;letter-spacing:.6px;margin-left:35px}
.hero-text h1{font-family:var(--head);font-weight:600;font-size:34px;line-height:38px;margin-top:3px}
.hero-text p{font-size:7.5px;line-height:11px;margin-top:5px;width:210px}

/* quick contact */
.qc-title{left:0;width:790px;top:354px;text-align:center;font-family:var(--head);font-weight:600;font-size:25px}
.qc-sub{left:0;width:790px;top:392px;text-align:center;font-size:7.5px;color:var(--muted)}

.form-card{left:74px;top:443px;width:341px;height:366px;background:var(--white);box-shadow:0 8px 24px rgba(0,0,0,.09)}
.eyebrow{left:107px;top:469px;display:flex;align-items:center;gap:8px;font-family:var(--head);font-weight:500;font-size:7px;color:var(--red);letter-spacing:.4px}
.eyebrow i{display:block;width:26px;height:1px;background:var(--red)}
.form-title{left:107px;top:484px;font-family:var(--head);font-weight:600;font-size:25px}
.form-lead{left:107px;top:522px;width:230px;font-size:7.3px;line-height:12px;color:var(--muted)}
.field{left:107px;width:270px;background:var(--field);font-family:var(--body);font-style:italic;font-size:7.3px;color:#888;padding-left:13px;display:flex;align-items:center}
.field.filled{color:var(--ink)}
.field .ico{position:absolute;right:12px;top:50%;margin-top:-7px;width:14px;height:14px;border:1px solid #222;border-radius:50%;display:flex;align-items:center;justify-content:center}
.field.msg{align-items:flex-start;padding-top:10px}
.field.msg .ico{top:10px;margin-top:0}
.submit{left:107px;top:743px;width:122px;height:29px;background:var(--red);clip-path:polygon(17px 0,100% 0,100% 100%,0 100%,0 17px);display:flex;align-items:center;justify-content:center;gap:5px;color:var(--white);font-family:var(--head);font-weight:600;font-size:8.5px;letter-spacing:.4px}
.hours-note{left:74px;width:346px;top:840px;text-align:center;font-family:var(--head);font-style:italic;font-size:10.5px}
.hours-note a{color:var(--red)}

.map{left:443px;top:432px;width:274px;height:376px;background:linear-gradient(135deg,#f0ebdf 0%,#eee4cf 45%,#e6e9e6 100%);clip-path:polygon(42px 0,100% 0,100% 100%,0 100%,0 42px)}
.info-card{left:492px;top:733px;width:176px}
.info-red{height:76px;background:var(--red);padding:15px 0 0 12px;color:var(--white);font-weight:700;font-size:7.2px;line-height:10.5px}
.info-row{display:flex;align-items:center;gap:8px}
.info-row + .info-row{margin-top:9px}
.w-circle{width:23px;height:23px;border-radius:50%;background:var(--white);flex:none;display:flex;align-items:center;justify-content:center}
.info-black{height:50px;background:var(--black);padding:0 0 0 12px;display:flex;align-items:center;gap:8px;color:var(--white);font-weight:700;font-size:11px;line-height:12.5px}
.r-circle{width:23px;height:23px;border-radius:50%;background:var(--red);flex:none;display:flex;align-items:center;justify-content:center}

/* footer */
.footer{left:0;top:936px;width:790px;height:264px;background:#141414}
.f-brand{left:74px;top:1015px;display:flex;align-items:center;gap:6px;color:var(--white);font-weight:700;font-size:12px}
.f-brand .dot{width:16px;height:16px;border-radius:50%;background:var(--red)}
.partner{background:var(--white)}
.f-head{top:976px;font-family:var(--head);font-weight:600;font-size:13px;color:var(--red)}
.f-links{left:242px;top:1002px;font-size:7.3px;color:#eee;line-height:21px;list-style:none}
.f-contact{left:334px;color:#eee;font-size:7.3px;line-height:10.5px;display:flex;align-items:center;gap:9px}
.f-contact .g-circle{width:19px;height:19px;border-radius:50%;background:#e5e5e5;flex:none;display:flex;align-items:center;justify-content:center}
.f-contact em{font-style:normal;color:var(--red)}
.f-map{left:522px;top:977px;width:194px;height:138px;background:linear-gradient(135deg,#eef1f2,#e4e9ea);clip-path:polygon(16px 0,100% 0,100% 100%,0 100%,0 16px)}
.social{top:1170px;width:19px;height:19px;border-radius:50%;border:1px solid #888;background:#333}
.copyright{right:72px;top:1180px;font-size:7.5px;color:var(--white)}
</style>
</head>
<body>

<header class="abs header"></header>
<svg class="abs" style="left:0;top:50px" width="260" height="32" viewBox="0 0 260 32">
  <polygon points="0,28 222,28 244,2 250,2 226,30 0,30" fill="var(--red)"/>
  <polygon points="230,30 254,2 258,2 234,30" fill="#aaa"/>
</svg>
<div class="abs brand"><span class="dot"></span>CALDER AUTOMOTIVE</div>

<div class="abs badge-top" style="left:341px">
  <div class="icon-ring"><svg width="11" height="11" viewBox="0 0 12 12"><circle cx="6" cy="5" r="3.5" fill="none" stroke="#333" stroke-width="1.3"/><path d="M4 8l-1 4 3-1.5 3 1.5-1-4" fill="#333"/></svg></div>
  <div class="txt"><span class="stars">★★★★★</span><br>5 Star Service</div>
</div>
<div class="abs badge-top" style="left:471px">
  <div class="icon-ring"><svg width="11" height="11" viewBox="0 0 12 12"><path d="M2 2l8 8M10 2L2 10" stroke="#333" stroke-width="1.6"/></svg></div>
  <div class="txt">Quality Service<br><b>Guarantee</b></div>
</div>
<div class="abs badge-top" style="left:606px">
  <div class="icon-ring"><svg width="11" height="11" viewBox="0 0 24 24"><path d="M6.6 10.8a15 15 0 006.6 6.6l2.2-2.2c.3-.3.7-.4 1-.2 1.1.4 2.3.6 3.6.6.6 0 1 .4 1 1V20c0 .6-.4 1-1 1A17 17 0 013 4c0-.6.4-1 1-1h3.5c.6 0 1 .4 1 1 0 1.3.2 2.5.6 3.6.1.3 0 .7-.2 1z" fill="#333"/></svg></div>
  <div class="txt">Call Us For Booking<br><b>555.013.9110</b></div>
</div>
<nav class="abs nav">
  <span>HOME</span><span>ABOUT US</span><span>SERVICES ⌄</span><span>GALLERY</span><span>TESTIMONIALS</span><span class="active">CONTACT US</span>
</nav>

<section class="abs hero" role="img" aria-label="Photo of a repair workshop interior with car lifts, workbenches and tool cabinets"></section>
<svg class="abs" style="left:0;top:80px" width="790" height="208" viewBox="0 0 790 208">
  <polygon points="0,0 403,0 230,208 0,208" fill="rgba(200,30,40,.45)"/>
</svg>
<div class="abs hero-text">
  <div class="kicker">CONTACT</div>
  <h1>Contact Us Today!</h1>
  <p>Quisque lorem neque, ultricies eget risus quis, fringilla interdum augue. Donec sollicitudin in ante sed consequat.</p>
</div>
<svg class="abs" style="left:0;top:287px" width="790" height="26" viewBox="0 0 790 26">
  <polygon points="217,0 790,0 790,14 722,20 680,10 247,24" fill="var(--red)"/>
</svg>

<h2 class="abs qc-title">Quick Contact</h2>
<p class="abs qc-sub">If you have any questions simply use the following contact details.</p>

<div class="abs form-card"></div>
<div class="abs eyebrow"><i></i>GET AN APPOINTMENT</div>
<h3 class="abs form-title">Leave A Message</h3>
<p class="abs form-lead">Lorem ipsum dolor sit amet, consectetur adipiscing elit, sed do eius tempor incididunt ut labore etdolore.</p>

<div class="abs field filled" style="top:569px;height:28px">Dana Whitfield |
  <span class="ico"><svg width="8" height="8" viewBox="0 0 10 10"><circle cx="5" cy="3" r="2.2" fill="#222"/><path d="M1 10a4 4 0 018 0z" fill="#222"/></svg></span></div>
<div class="abs field" style="top:600px;height:28px">+ 00 123 456 7890
  <span class="ico"><svg width="8" height="8" viewBox="0 0 24 24"><path d="M6.6 10.8a15 15 0 006.6 6.6l2.2-2.2c.3-.3.7-.4 1-.2 1.1.4 2.3.6 3.6.6.6 0 1 .4 1 1V20c0 .6-.4 1-1 1A17 17 0 013 4c0-.6.4-1 1-1h3.5c.6 0 1 .4 1 1 0 1.3.2 2.5.6 3.6.1.3 0 .7-.2 1z" fill="#222"/></svg></span></div>
<div class="abs field" style="top:631px;height:28px">hello@danawhitfield.com
  <span class="ico"><svg width="8" height="6" viewBox="0 0 10 7"><rect width="10" height="7" fill="#222"/><path d="M0 0l5 4 5-4" stroke="#fff" fill="none"/></svg></span></div>
<div class="abs field msg" style="top:661px;height:68px">Message
  <span class="ico"><svg width="8" height="8" viewBox="0 0 10 10"><path d="M1 9l1-3 5-5 2 2-5 5z" fill="#222"/></svg></span></div>
<div class="abs submit"><svg width="9" height="9" viewBox="0 0 10 10"><path d="M10 0L0 4l4 2 2 4z" fill="#fff"/></svg>SUBMIT</div>
<p class="abs hours-note">We're open for business 5 days a week. See the <a>opening hours</a> of our workshop</p>

<div class="abs map" role="img" aria-label="Street map showing the workshop location"></div>
<div class="abs info-card">
  <div class="info-red">
    <div class="info-row"><span class="w-circle"><svg width="10" height="12" viewBox="0 0 10 13"><path d="M5 0a5 5 0 015 5c0 4-5 8-5 8S0 9 0 5a5 5 0 015-5z" fill="#000"/><circle cx="5" cy="5" r="2" fill="#fff"/></svg></span>418 Harbor Loop #5<br>Brookdale, TX 75000</div>
    <div class="info-row"><span class="w-circle"><svg width="10" height="7" viewBox="0 0 10 7"><rect width="10" height="7" fill="#000"/><path d="M0 0l5 4 5-4" stroke="#fff" fill="none"/></svg></span>CalderAutoLLC@mailbox.com</div>
  </div>
  <div class="info-black"><span class="r-circle"><svg width="11" height="11" viewBox="0 0 24 24"><path d="M6.6 10.8a15 15 0 006.6 6.6l2.2-2.2c.3-.3.7-.4 1-.2 1.1.4 2.3.6 3.6.6.6 0 1 .4 1 1V20c0 .6-.4 1-1 1A17 17 0 013 4c0-.6.4-1 1-1h3.5c.6 0 1 .4 1 1 0 1.3.2 2.5.6 3.6.1.3 0 .7-.2 1z" fill="#fff"/></svg></span>555.013.9110<br>555.014.7493</div>
</div>
<svg class="abs" style="left:492px;top:808px" width="30" height="26" viewBox="0 0 30 26"><polygon points="0,0 28,0 0,26" fill="var(--red)"/></svg>

<footer class="abs footer"></footer>
<div class="abs f-brand"><span class="dot"></span>CALDER AUTOMOTIVE</div>
<div class="abs partner" style="left:74px;top:1089px;width:61px;height:24px"></div>
<div class="abs partner" style="left:139px;top:1089px;width:49px;height:24px"></div>
<div class="abs partner" style="left:74px;top:1116px;width:33px;height:24px"></div>
<div class="abs partner" style="left:110px;top:1116px;width:60px;height:24px"></div>

<h4 class="abs f-head" style="left:242px">Quick Links.</h4>
<ul class="abs f-links"><li>Home</li><li>About Us</li><li>Services</li><li>Gallery</li><li>Testimonials</li><li>Contact Us</li></ul>

<h4 class="abs f-head" style="left:339px">Contact Us</h4>
<div class="abs f-contact" style="top:1005px"><span class="g-circle"><svg width="8" height="10" viewBox="0 0 10 13"><path d="M5 0a5 5 0 015 5c0 4-5 8-5 8S0 9 0 5a5 5 0 015-5z" fill="#555"/><circle cx="5" cy="5" r="2" fill="#e5e5e5"/></svg></span><span>418 Harbor Loop #5<br>Brookdale, TX 75000</span></div>
<div class="abs f-contact" style="top:1036px"><span class="g-circle"><svg width="9" height="9" viewBox="0 0 24 24"><path d="M6.6 10.8a15 15 0 006.6 6.6l2.2-2.2c.3-.3.7-.4 1-.2 1.1.4 2.3.6 3.6.6.6 0 1 .4 1 1V20c0 .6-.4 1-1 1A17 17 0 013 4c0-.6.4-1 1-1h3.5c.6 0 1 .4 1 1 0 1.3.2 2.5.6 3.6.1.3 0 .7-.2 1z" fill="#555"/></svg></span><span><em>OFFICE:</em> 555.013.9110<br><em>Phone:</em> 555.014.7493</span></div>
<div class="abs f-contact" style="top:1069px"><span class="g-circle"><svg width="8" height="6" viewBox="0 0 10 7"><rect width="10" height="7" fill="#555"/><path d="M0 0l5 4 5-4" stroke="#e5e5e5" fill="none"/></svg></span><span>CalderAutoLLC@mailbox.com</span></div>
<div class="abs f-contact" style="top:1100px"><span class="g-circle"><svg width="9" height="9" viewBox="0 0 10 10"><circle cx="5" cy="5" r="4.5" fill="#555"/><path d="M5 2v3h2" stroke="#e5e5e5" fill="none"/></svg></span><span><em>Hours of Operation:</em> M-F 8:30-6pm</span></div>

<div class="abs f-map" role="img" aria-label="Small street map of the shop neighbourhood"></div>

<div class="abs social" style="left:100px"></div>
<div class="abs social" style="left:122px"></div>
<div class="abs social" style="left:144px"></div>

<svg class="abs" style="left:0;top:1170px" width="790" height="30" viewBox="0 0 790 30">
  <polygon points="222,30 246,1 790,1 790,30" fill="var(--red)"/>
  <polygon points="0,28 205,28 204,30 0,30" fill="var(--red)"/>
  <polygon points="206,30 230,1 236,1 212,30" fill="#aaa"/>
</svg>
<p class="abs copyright">Copyright © 2024 Calder Automotive LLC. All Rights Reserved.</p>

</body>
</html>
```